Business Card Design Project

it should have the logo in one side
the other side

Name
Position
telephone
email

Target Market(s)

Business prospects and upscale Fashion shoppers

Industry/Entity Type

Business

Font styles to use
Serif
Sans Serif

Requirements
Must have
• very elegant, upscale, modern
Nice to have
• layering, embossed
Should not have
• Should not use any color OTHER THAN black, silver, white or purple

```html
<!DOCTYPE html>
<html lang="en">
<head>
<meta charset="utf-8">
<title>Velora Luxury Boutique – Business Card</title>
<link rel="stylesheet" href="https://fonts.googleapis.com/css2?family=Josefin+Sans:wght@400&family=Montserrat:wght@600;700&family=Playfair+Display:wght@700&display=swap">
<style>
  :root {
    --backdrop: #a7a7a7;
    --card: #f5f5f5;
    --ink: #111111;
    --purple: #8b4aa6;
    --purple-deep: #5e2a78;
    --silver: #dedede;
  }
  * { margin: 0; padding: 0; box-sizing: border-box; }
  html, body { width: 1200px; height: 900px; overflow: hidden; }
  body {
    background: var(--backdrop);
    position: relative;
    font-family: "Montserrat", sans-serif;
  }
  .card {
    position: absolute;
    top: 290px;
    width: 540px;
    height: 310px;
    background: var(--card);
    border-radius: 18px;
    overflow: hidden;
  }
  .card--front { left: 40px; }
  .card--back { left: 620px; }

  /* brand lockup */
  .brand { position: absolute; }
  .brand__mark {
    display: block;
    background: linear-gradient(180deg, var(--purple-deep), var(--purple));
  }
  .brand__name {
    font-family: "Josefin Sans", sans-serif;
    font-weight: 400;
    color: var(--ink);
    letter-spacing: 0.04em;
    line-height: 1;
  }
  .brand__tagline {
    font-family: "Playfair Display", serif;
    font-weight: 700;
    color: var(--ink);
    text-transform: uppercase;
    letter-spacing: 0.14em;
    line-height: 1;
  }

  .card--front .brand { left: 30px; top: 34px; text-align: center; }
  .card--front .brand__mark { width: 56px; height: 56px; margin: 0 auto 12px; }
  .card--front .brand__name { font-size: 38px; }
  .card--front .brand__tagline { font-size: 10px; margin-top: 6px; }

  .person {
    position: absolute;
    right: 34px;
    top: 180px;
    text-align: right;
    font-weight: 700;
    line-height: 1.15;
  }
  .person__name { color: var(--purple); font-size: 19px; letter-spacing: -0.02em; }
  .person__role { color: var(--ink); font-size: 15px; letter-spacing: -0.02em; }

  .divider {
    position: absolute;
    left: 26px;
    right: 34px;
    top: 232px;
    height: 5px;
    background: var(--ink);
  }
  .contact {
    position: absolute;
    left: 26px;
    top: 246px;
    list-style: none;
    font-weight: 600;
    font-size: 15px;
    color: var(--ink);
    line-height: 1.3;
  }
  .contact__item { display: flex; align-items: center; gap: 10px; }
  .contact__icon { width: 14px; height: 14px; fill: var(--purple); flex: none; }

  /* back side */
  .backdrop-word {
    position: absolute;
    left: -20px;
    top: 60px;
    font-family: "Josefin Sans", sans-serif;
    font-size: 170px;
    line-height: 1;
    color: var(--silver);
    letter-spacing: 0.02em;
  }
  .card--back .brand { right: 28px; top: 62px; text-align: center; }
  .card--back .brand__mark { width: 96px; height: 96px; margin: 0 auto 16px; }
  .card--back .brand__name { font-size: 52px; }
  .card--back .brand__tagline { font-size: 13px; margin-top: 8px; }
</style>
</head>
<body>
  <section class="card card--front" aria-label="Card front">
    <div class="brand">
      <span class="brand__mark"></span>
      <div class="brand__name">VELORA</div>
      <div class="brand__tagline">Luxury Boutique</div>
    </div>

    <div class="person">
      <div class="person__name">YOUR NAMME</div>
      <div class="person__role">DSIGNATION</div>
    </div>

    <div class="divider"></div>

    <ul class="contact">
      <li class="contact__item">
        <svg class="contact__icon" viewBox="0 0 16 16" aria-hidden="true"><path d="M2 5c0-2 2-3 6-3s6 1 6 3v1h-3V5H5v1H2zM4 7h8l2 7H2z"/></svg>
        <span>0900 555 0142</span>
      </li>
      <li class="contact__item">
        <svg class="contact__icon" viewBox="0 0 16 16" aria-hidden="true"><path d="M1 3h14v10H1zM2 4.5v.6l6 4 6-4v-.6z"/></svg>
        <span>hello@velorashop.com</span>
      </li>
    </ul>
  </section>

  <section class="card card--back" aria-label="Card back">
    <div class="backdrop-word" aria-hidden="true">VEL</div>
    <div class="brand">
      <span class="brand__mark"></span>
      <div class="brand__name">VELORA</div>
      <div class="brand__tagline">Luxury Boutique</div>
    </div>
  </section>
</body>
</html>
```